Bright Pelvic Health Business Card

Need a business card for a surgical practice called Bright Pelvic Health. We have recently selected a logo (attached). The business card will need to have two formats:
1) One with the logo/physician name/ contact info on the front and location information on the back.
2) One in "appointment reminder card" style with the logo/ contact info/ date/ time on the front and the location information on the back.

The front side should include the following information:
- Logo
- Ravi K. Desai, MD FACOG
- phone: 469-555-0182
- fax: 1-469-555-0147
- email: admin@brightpelvic.example
- website: www.brightpelvichealth.example

The back side should have the office locations listed:
4812 Quarry Bend Dr, Plano, TX 75093
3650 Wrenfield Rd, Plano, TX 75025
2245 Brambleton Ln, Irving, TX 75038
915 S Garnet Ave B314, Dallas, TX 75201
1836 Tillman Pkwy, Grand Prairie, TX 75051
6417 Dorrance Way Dr, San Antonio, TX 78240
5920 Kessler Rd, Pasadena, TX 77504

Target Market(s)

1. Other physicians who might refer patients
2. Female patients

Industry/Entity Type

Business

Font styles to use
Other font styles liked:
• Tahoma for lettering

Requirements
Must have
• As per the instructions
Should not have
• No other images needed -- please try to keep font consistent with logo design. Can use Tahoma as the font for lettering.

```html
<!DOCTYPE html>
<html lang="en">
<head>
<meta charset="utf-8">
<title>Bright Pelvic Health – Business and Appointment Cards</title>
<link rel="stylesheet" href="https://fonts.googleapis.com/css2?family=PT+Sans:wght@400;700&display=swap">
<style>
  :root {
    --brand-blue: #1c5ca8;
    --deep-blue: #1a4f9c;
    --teal: #3db4c6;
    --ink: #111;
    --card-top: #ffffff;
    --card-bottom: #ececec;
    --motif-pink: rgba(232, 120, 130, 0.32);
    --motif-blue: rgba(150, 175, 215, 0.28);
    --page: #ffffff;
  }
  * { box-sizing: border-box; margin: 0; padding: 0; }
  html, body { width: 1200px; height: 900px; overflow: hidden; background: var(--page); }
  body { position: relative; font-family: "PT Sans", Tahoma, sans-serif; }

  .brand-title {
    position: absolute; top: 188px; left: 0; width: 1200px;
    text-align: center; font-size: 32px; font-weight: 700; color: var(--brand-blue);
    letter-spacing: 0.2px;
  }

  .card {
    position: absolute; width: 422px; height: 240px; overflow: hidden;
    background: linear-gradient(180deg, var(--card-top) 0%, var(--card-top) 45%, var(--card-bottom) 100%);
    box-shadow: 4px 8px 16px rgba(0,0,0,0.28);
    text-align: center;
  }
  .card--business-front { left: 85px; top: 268px; }
  .card--business-back  { left: 85px; top: 546px; }
  .card--reminder-front { left: 697px; top: 268px; }
  .card--reminder-back  { left: 697px; top: 546px; }

  .card-motif { position: absolute; inset: 0; }
  .card-motif--front {
    background:
      radial-gradient(ellipse 90px 110px at 20px 200px, var(--motif-pink), transparent 70%),
      radial-gradient(ellipse 90px 110px at 402px 200px, var(--motif-pink), transparent 70%);
  }
  .card-motif--back {
    background:
      radial-gradient(ellipse 90px 140px at 211px 130px, var(--motif-blue), transparent 75%),
      radial-gradient(ellipse 110px 110px at 30px 160px, var(--motif-pink), transparent 70%),
      radial-gradient(ellipse 110px 110px at 392px 160px, var(--motif-pink), transparent 70%);
  }

  .card-content { position: relative; }

  .card-brand { color: var(--brand-blue); font-weight: 700; }
  .card--business-front .card-brand { margin-top: 76px; font-size: 21px; }
  .card--reminder-front .card-brand { margin-top: 54px; font-size: 16px; }

  .physician-name {
    margin-top: 34px; font-size: 17px; font-weight: 700; color: var(--teal); letter-spacing: 0.5px;
  }
  .physician-name .credentials { font-size: 13px; }

  .contact-grid {
    position: absolute; top: 185px; left: 14px; right: 16px;
    display: grid; grid-template-columns: auto 1fr; column-gap: 10px; row-gap: 6px;
    font-size: 12.5px; line-height: 17px; white-space: nowrap; text-align: left;
  }
  .contact-grid .right { text-align: right; }
  .label { color: var(--teal); }
  .value { color: var(--deep-blue); }

  .contact-stack { margin-top: 18px; font-size: 12px; line-height: 16px; }
  .contact-stack .gap { margin-top: 5px; }

  .appointment-fields {
    margin: 12px 0 0 128px; text-align: left; font-size: 13px; font-weight: 700; color: var(--teal);
  }
  .appointment-fields .field { display: flex; align-items: baseline; height: 24px; }
  .appointment-fields .field--time { color: var(--deep-blue); }
  .appointment-fields .field-line {
    margin-left: 4px; width: 124px; border-bottom: 1px dotted var(--deep-blue);
  }

  .location-list {
    list-style: none; padding-top: 58px; font-size: 12px; line-height: 19.5px;
  }
  .location-list li:nth-child(odd) { color: var(--deep-blue); }
  .location-list li:nth-child(even) { color: var(--teal); }

  .caption {
    position: absolute; top: 826px; font-size: 18px; color: var(--ink); letter-spacing: 0.3px;
  }
  .caption--business { left: 100px; }
  .caption--reminder { left: 648px; }
</style>
</head>
<body>

  <div class="brand-title">Bright Pelvic Health</div>

  <section class="card card--business-front">
    <div class="card-motif card-motif--front" role="img" aria-label="Faint pink brand motif curving along the lower edges"></div>
    <div class="card-content">
      <div class="card-brand">Bright Pelvic Health</div>
      <div class="physician-name">Ravi K. Desai, <span class="credentials">MD FACOG</span></div>
    </div>
    <div class="contact-grid">
      <div><span class="label">phone:</span> <span class="value">469-555-0182</span></div>
      <div class="right"><span class="label">email:</span> <span class="value">admin@brightpelvic.example</span></div>
      <div><span class="label">fax:</span> <span class="value">1-469-555-0147</span></div>
      <div class="right"><span class="label">website:</span> <span class="value">www.brightpelvichealth.example</span></div>
    </div>
  </section>

  <section class="card card--business-back">
    <div class="card-motif card-motif--back" role="img" aria-label="Faint large brand motif in soft blue and pink behind the address list"></div>
    <div class="card-content">
      <ul class="location-list">
        <li>4812 Quarry Bend Dr, Plano, TX 75093</li>
        <li>3650 Wrenfield Rd, Plano, TX 75025</li>
        <li>2245 Brambleton Ln, Irving, TX 75038</li>
        <li>915 S Garnet Ave B314, Dallas, TX 75201</li>
        <li>1836 Tillman Pkwy, Grand Prairie, TX 75051</li>
        <li>6417 Dorrance Way Dr, San Antonio, TX 78240</li>
        <li>5920 Kessler Rd, Pasadena, TX 77504</li>
      </ul>
    </div>
  </section>

  <section class="card card--reminder-front">
    <div class="card-motif card-motif--front" role="img" aria-label="Faint pink brand motif curving along the sides"></div>
    <div class="card-content">
      <div class="card-brand">Bright Pelvic Health</div>
      <div class="contact-stack">
        <div><span class="label">phone:</span> <span class="value">469-555-0182</span></div>
        <div><span class="label">fax:</span> <span class="value">1-469-555-0147</span></div>
        <div class="gap"><span class="label">email:</span> <span class="value">admin@brightpelvic.example</span></div>
        <div><span class="label">website:</span> <span class="value">www.brightpelvichealth.example</span></div>
      </div>
      <div class="appointment-fields">
        <div class="field field--date">DATE:<span class="field-line"></span></div>
        <div class="field field--time">TIME:<span class="field-line"></span></div>
      </div>
    </div>
  </section>

  <section class="card card--reminder-back">
    <div class="card-motif card-motif--back" role="img" aria-label="Faint large brand motif in soft blue and pink behind the address list"></div>
    <div class="card-content">
      <ul class="location-list">
        <li>4812 Quarry Bend Dr, Plano, TX 75093</li>
        <li>3650 Wrenfield Rd, Plano, TX 75025</li>
        <li>2245 Brambleton Ln, Irving, TX 75038</li>
        <li>915 S Garnet Ave B314, Dallas, TX 75201</li>
        <li>1836 Tillman Pkwy, Grand Prairie, TX 75051</li>
        <li>6417 Dorrance Way Dr, San Antonio, TX 78240</li>
        <li>5920 Kessler Rd, Pasadena, TX 77504</li>
      </ul>
    </div>
  </section>

  <p class="caption caption--business">Bright Pelvic Health Business Card_2</p>
  <p class="caption caption--reminder">Double-sided "appointment reminder card" Design_2</p>

</body>
</html>
```